Cleaning and Maintenance Business card design

i provide a service which includes;
Professional Window Cleaning
Lawn Mowing
Gardening
Painting
Rubbish Removal
Commercial Cleaning
Property & Ground Maintenance
Pensioner discounts apply
Call now for an inquiry and free quote
`Double sided` (willing to pay any extra)
i would like a design that is not too crowded and straight to the point.
i want the reader to know exactly what the business is about from one glance.
i would like the logo to communicate the businesses 3 main aspects (window cleaning, lawn mowing, and Cleaning)
Thanks.
Industry/Entity Type
Business
Contact Information for Business Card
Business name : Brick 4 Bloom*
* with subline 'And Everything In Between' (smaller font)
Name: Tom Vasharoukis
Mobile: 0417 952 164
Email: t.vasharoukis@pebblemail.net
ABN: 37 514 209 861
`Double Sided`
Logo Text
Brick 4 Bloom
Logo styles of interest
Character Logo
Look and feel

```html
<!DOCTYPE html>
<html lang="en">
<head>
<meta charset="utf-8">
<title>Brick 4 Bloom – Business Card</title>
<link rel="stylesheet" href="https://fonts.googleapis.com/css2?family=Lato:wght@300;400;700;900&display=swap">
<style>
  :root {
    --page-bg: #e9e2d8;
    --card-white: #ffffff;
    --card-shadow: rgba(60, 45, 30, 0.18);
    --band-black: #111111;
    --band-blue: #0fb0e6;
    --band-blue-dark: #08465a;
    --brand-green: #2f8f2a;
    --grass-light: #9bd84a;
    --grass-mid: #5fae25;
    --grass-deep: #2f7a12;
    --text-dark: #2a2a2a;
    --text-grey: #555555;
    --text-soft: #8a8a8a;
  }
  * { box-sizing: border-box; margin: 0; padding: 0; }
  html, body { width: 1200px; height: 744px; overflow: hidden; }
  body {
    background: var(--page-bg);
    font-family: "Lato", "Helvetica Neue", Arial, sans-serif;
    display: flex;
    align-items: center;
    justify-content: center;
    gap: 60px;
  }
  .card {
    position: relative;
    width: 520px;
    height: 317px;
    background: var(--card-white);
    box-shadow: 0 10px 28px var(--card-shadow);
    overflow: hidden;
  }

  /* Front side */
  .card-front .brand-block {
    position: absolute;
    top: 46px;
    left: 0;
    width: 100%;
    text-align: center;
    z-index: 1;
  }
  .card-front .brand-name {
    font-weight: 900;
    font-size: 44px;
    line-height: 50px;
    letter-spacing: 1px;
    color: var(--brand-green);
  }
  .card-front .brand-subline {
    margin-top: 4px;
    font-weight: 400;
    font-size: 15px;
    line-height: 20px;
    letter-spacing: 2px;
    color: var(--text-grey);
  }
  .card-front .services {
    margin-top: 8px;
    font-weight: 700;
    font-size: 13px;
    line-height: 18px;
    letter-spacing: 1px;
    text-transform: uppercase;
    color: var(--band-blue);
  }
  .card-front .grass-photo {
    position: absolute;
    left: 0;
    bottom: 0;
    width: 100%;
    height: 150px;
    background: linear-gradient(180deg,
      rgba(255,255,255,0) 0%,
      var(--grass-light) 35%,
      var(--grass-mid) 70%,
      var(--grass-deep) 100%);
  }

  /* Back side */
  .card-back .top-band {
    position: absolute;
    top: 24px;
    left: 0;
    width: 100%;
    height: 46px;
    background: var(--band-black);
  }
  .card-back .side-stripe {
    position: absolute;
    top: 0;
    left: 0;
    width: 100%;
    height: 100%;
  }
  .card-back .brand-name {
    position: absolute;
    top: 30px;
    left: 60px;
    font-weight: 900;
    font-size: 26px;
    line-height: 34px;
    color: var(--brand-green);
  }
  .card-back .brand-subline {
    position: absolute;
    top: 78px;
    left: 60px;
    font-weight: 400;
    font-size: 12px;
    line-height: 16px;
    letter-spacing: 1.5px;
    color: var(--text-soft);
  }
  .card-back .contact {
    position: absolute;
    top: 118px;
    left: 60px;
    color: var(--text-dark);
  }
  .card-back .contact-name {
    font-weight: 400;
    font-size: 16px;
    margin-bottom: 30px;
  }
  .card-back .contact-line {
    font-weight: 300;
    font-size: 14px;
    line-height: 22px;
    color: var(--text-grey);
  }
</style>
</head>
<body>

  <section class="card card-front" aria-label="Card front">
    <div class="brand-block">
      <div class="brand-name">Brick 4 Bloom</div>
      <div class="brand-subline">And Everything In Between</div>
      <div class="services">Window Cleaning · Lawn Mowing · Cleaning</div>
    </div>
    <div class="grass-photo" role="img" aria-label="Photograph of fresh green grass blades rising along the bottom of the card"></div>
  </section>

  <section class="card card-back" aria-label="Card back">
    <div class="top-band"></div>
    <svg class="side-stripe" viewBox="0 0 520 317" aria-hidden="true">
      <polygon points="370,0 450,0 482,317 400,317" fill="var(--band-blue)"/>
      <polygon points="372,24 452,24 457,70 377,70" fill="var(--band-blue-dark)"/>
    </svg>
    <div class="brand-name">Brick 4 Bloom</div>
    <div class="brand-subline">And Everything In Between</div>
    <div class="contact">
      <p class="contact-name">Tom Vasharoukis</p>
      <p class="contact-line">Mobile: 0417 952 164</p>
      <p class="contact-line">Email: t.vasharoukis@pebblemail.net</p>
      <p class="contact-line">ABN: 37 514 209 861</p>
    </div>
  </section>

</body>
</html>
```